Puslishing House Needs poster Design for Medical Book

We need an advertisement desing for a medical book on cardiology named "Lumivarte" (Hypertension), which 2nd Edition we launched last August. What makes this book special is that this is the first time in history that a hypertension book has a second edition in Brazil and was written by the Vessel Studies Unit of the Austral Guild of Circulatory Medicine in comemoration in its 100 years. The two news about this book is that we sold 1000 units since we launched (which is good) and we have now an ebook version for all tablet, smartphones and readers. From this month on it is going to happen importants hypertension meetings and we want to promote this two news about this book - 1000 units sold and ebook version. We would like to see designs that use orange (the publishing house color) and communicate celebration.

Target Market(s)

Doctors Specialist from several segments like Cardiology, Endocrinology, Nephrology, Nutrition. Most of the target are man with 50 years-old.

Industry/Entity Type

Medical

Requirements
Must have
• The adverstisement must have the attached book cover and publishing house logo (Quorvane) using only the name (without the tree) or the complete logo.
Should not have
• The design should not use old-style, serif fonts like Times new Roman.

```html
<!DOCTYPE html>
<html lang="en">
<head>
<meta charset="utf-8">
<title>Lumivarte – 1000 units sold · ebook version</title>
<link rel="stylesheet" href="https://fonts.googleapis.com/css2?family=Bebas+Neue&family=Oswald:wght@500;600&family=Montserrat:wght@500;700;800&display=swap">
<style>
  :root{
    --forest:#1c5a34;
    --forest-deep:#0f3f22;
    --lavender:#e9e8f6;
    --coral:#f1563a;
    --coral-deep:#e24a30;
    --ink:#141414;
    --paper:#ffffff;
  }
  html,body{margin:0;padding:0;overflow:hidden;background:var(--lavender);}
  .poster{
    position:relative;width:863px;height:1200px;overflow:hidden;
    background:var(--lavender);font-family:"Montserrat",Arial,sans-serif;color:var(--ink);
  }
  .top-band{
    position:absolute;left:0;top:0;width:100%;height:64px;
    background:linear-gradient(90deg,var(--forest-deep),var(--forest) 50%,var(--forest-deep));
    display:flex;align-items:center;justify-content:center;
  }
  .top-band p{
    margin:0;font-family:"Oswald",Arial,sans-serif;font-weight:600;
    font-size:19px;letter-spacing:.6px;color:var(--paper);text-transform:uppercase;
  }
  .title{
    position:absolute;left:0;width:100%;top:108px;margin:0;text-align:center;
    font-family:"Bebas Neue",Impact,sans-serif;font-weight:400;font-size:168px;line-height:1;
    color:var(--coral);letter-spacing:2px;
  }
  .rule{position:absolute;left:95px;width:673px;height:3px;background:var(--forest);}
  .rule--one{top:258px}
  .rule--two{top:376px}
  .headline{position:absolute;left:95px;width:673px;margin:0;}
  .headline strong{
    display:block;font-weight:800;line-height:1;color:var(--ink);letter-spacing:-.5px;
  }
  .headline small{display:block;font-weight:700;color:var(--ink);}
  .units{top:272px}
  .units strong{font-size:76px;text-align:center}
  .units small{font-size:14px;margin-top:2px;padding-left:4px}
  .ebook{top:392px}
  .ebook strong{font-size:88px;text-align:center}
  .ebook small{font-size:13.5px;margin-top:0;text-align:center;font-weight:600}
  .swoosh{position:absolute;left:0;top:0;width:863px;height:1200px}
  .book-art{
    position:absolute;left:243px;top:530px;width:426px;height:540px;
    background:linear-gradient(160deg,#1f5a3a 0%,#3f7d5a 40%,#dfe8e2 75%,#f4f6f5 100%);
    border-radius:4px;
  }
  .footer{position:absolute;left:0;top:1100px;width:100%;height:80px;color:var(--paper);}
  .partner-badge{
    position:absolute;left:38px;top:8px;width:54px;height:54px;border-radius:50%;
    background:#2e5fa8;
  }
  .society{
    position:absolute;left:108px;top:12px;width:280px;display:flex;align-items:center;gap:10px;
  }
  .society .dot{flex:none;width:40px;height:40px;border-radius:50%;background:var(--paper);}
  .society span{font-size:11.5px;font-weight:700;line-height:1.25;text-transform:uppercase;}
  .site{position:absolute;left:400px;top:44px;font-size:10px;font-weight:500;}
  .publisher{
    position:absolute;right:38px;top:-14px;width:90px;height:92px;
    display:flex;flex-direction:column;align-items:center;justify-content:flex-end;gap:6px;
  }
  .publisher .mark{width:74px;height:62px;border:2px solid var(--paper);box-sizing:border-box;}
  .publisher span{font-size:14px;font-weight:700;letter-spacing:1px;text-transform:uppercase;}
</style>
</head>
<body>
<main class="poster">
  <header class="top-band">
    <p>First time in history that a hypertension book has a second edition in Brazil</p>
  </header>

  <h1 class="title">LUMIVARTE</h1>
  <div class="rule rule--one"></div>
  <h2 class="headline units"><strong>1000 units sold</strong><small>Since launched</small></h2>
  <div class="rule rule--two"></div>
  <h2 class="headline ebook"><strong>ebook version</strong><small>now an ebook version is available for all tablet, smartphones and readers</small></h2>

  <svg class="swoosh" viewBox="0 0 863 1200" aria-hidden="true">
    <path d="M0 582 C260 598 610 690 863 898 L863 930 C600 725 250 628 0 612 Z" fill="var(--forest)"/>
    <path d="M0 612 C250 628 600 725 863 930 L863 1200 L0 1200 Z" fill="var(--coral)"/>
  </svg>

  <div class="book-art" role="img" aria-label="Lumivarte 2nd edition book cover, standing upright on a second copy lying flat, showing a blood pressure gauge"></div>

  <footer class="footer">
    <div class="partner-badge"></div>
    <div class="society">
      <div class="dot"></div>
      <span>Vessel Studies Unit of the Austral Guild of Circulatory Medicine</span>
    </div>
    <span class="site">www.quorvane.com.br</span>
    <div class="publisher">
      <div class="mark"></div>
      <span>Quorvane</span>
    </div>
  </footer>
</main>
</body>
</html>
```